One slide graphic for website

I am designing a series of sliders for my website http://new.kelmarbyte.com

The slide I am trying to create has the following message:

EVERY company is a media company.
Empower yours now!

Learn More >

The ideas I have had for imagery are an office building with the letters 'Every Company is a Media Company' either shone onto the building or letters on the building roof ledge ect.

Aby ideas you may have to improve on this would be appreciated.

The idea behind the slide is to promote a software application which gives marketing professionals the chance to increase their media coverage. The message also encourages companies to create their own news on a number of platforms as the media landscape has changed so much. Look at the blue finch stunt whereby they generated 10 million views on viddlo using PR alone.

Good luck and I look forward to seeing your ideas.

Marcus

```html
<!DOCTYPE html>
<html lang="en">
<head>
<meta charset="utf-8">
<title>Kelmarbyte – Every company is a media company</title>
<link rel="stylesheet" href="https://fonts.googleapis.com/css2?family=Open+Sans:ital,wght@0,300;0,400;0,600;0,700;1,300;1,400;1,700&display=swap">
<style>
  :root {
    --green: #23944a;
    --green-dark: #1c7a3c;
    --green-stripe: #15692f;
    --orange: #f7941d;
    --purple: #8a3fa8;
    --ink: #444444;
    --ink-soft: #5a5a5a;
    --white: #ffffff;
    --sky-top: #7fb3e6;
    --sky-mid: #3f77b3;
    --glass-dark: #1f3b63;
    --caption-bg: rgba(40, 52, 66, 0.78);
  }
  * { box-sizing: border-box; margin: 0; padding: 0; }
  html, body { width: 1200px; height: 849px; overflow: hidden; background: var(--white); }
  body { font-family: "Open Sans", Arial, sans-serif; color: var(--ink); position: relative; }

  .site-header { position: absolute; left: 0; top: 0; width: 1200px; height: 111px; }
  .brand { position: absolute; left: 146px; top: 34px; display: flex; align-items: center; gap: 8px; }
  .brand-name { font-size: 34px; font-weight: 400; color: var(--green); letter-spacing: -0.5px; line-height: 1; }
  .brand-dot { width: 14px; height: 14px; border-radius: 50%; background: var(--green); }

  .contact-bar { position: absolute; right: 164px; top: 17px; display: flex; align-items: center; gap: 9px; }
  .phone { font-size: 18px; color: #666; font-weight: 400; margin-right: 2px; }
  .social { width: 21px; height: 21px; border-radius: 50%; background: #4a4a4a; }

  .action-buttons { position: absolute; right: 164px; top: 52px; display: flex; gap: 6px; }
  .action { height: 27px; border-radius: 7px; color: var(--white); font-weight: 700; font-style: italic;
            font-size: 15px; display: flex; align-items: center; padding: 0 10px 0 6px; gap: 7px; }
  .action-demo { background: var(--purple); width: 126px; }
  .action-login { background: var(--orange); width: 88px; }
  .action svg { width: 18px; height: 18px; flex: none; }

  .main-nav { position: absolute; left: 0; top: 111px; width: 1200px; height: 47px;
              background: linear-gradient(var(--green) 0%, var(--green-dark) 100%);
              border-top: 4px solid var(--green-stripe); }
  .main-nav ul { list-style: none; display: flex; position: absolute; left: 145px; top: 0; height: 43px; }
  .main-nav li { font-size: 12.5px; font-weight: 700; color: var(--white); padding: 0 14px; height: 43px;
                 line-height: 43px; border-right: 1px solid rgba(0,0,0,0.15); white-space: nowrap; }
  .main-nav li.is-active { background: var(--orange); }

  .hero { position: absolute; left: 0; top: 158px; width: 1200px; height: 415px; overflow: hidden;
          background: linear-gradient(90deg, var(--glass-dark) 0%, var(--sky-mid) 22%, var(--sky-top) 45%, #a9cff2 55%, var(--sky-mid) 75%, var(--glass-dark) 100%); }
  .hero-caption { position: absolute; left: 170px; top: 128px; width: 830px; height: 85px; background: var(--caption-bg);
                  text-align: center; color: var(--white); font-size: 32px; line-height: 41px; padding-top: 2px; }
  .hero-cta { position: absolute; left: 508px; top: 225px; width: 185px; height: 50px; border-radius: 25px 25px 25px 25px;
              background: var(--green); color: var(--white); font-size: 22px; text-align: center; line-height: 50px; }

  .tagline { position: absolute; left: 0; top: 585px; width: 1200px; text-align: center; font-size: 33px;
             font-weight: 300; font-style: italic; line-height: 36px; color: var(--ink); }

  .features { position: absolute; left: 146px; top: 697px; display: flex; gap: 10px; }
  .feature { width: 218px; height: 160px; text-align: center; overflow: hidden;
             box-shadow: 0 0 6px rgba(0,0,0,0.08); border-radius: 2px; }
  .feature h2 { font-size: 23px; font-weight: 400; font-style: italic; color: var(--ink); margin-top: 0; line-height: 30px; }
  .feature svg { display: block; margin: 12px auto 0; width: 80px; height: 76px; }
  .feature p { font-size: 12.5px; font-style: italic; color: var(--ink-soft); line-height: 18px; margin: 10px 22px 0; }
</style>
</head>
<body>
  <header class="site-header">
    <div class="brand">
      <span class="brand-name">KELMARBYTE</span>
      <span class="brand-dot"></span>
    </div>
    <div class="contact-bar">
      <span class="phone">t. +44 (0)1632 960418</span>
      <span class="social" aria-label="Social link"></span>
      <span class="social" aria-label="Social link"></span>
      <span class="social" aria-label="Social link"></span>
    </div>
    <div class="action-buttons">
      <span class="action action-demo">
        <svg viewBox="0 0 18 18"><circle cx="9" cy="9" r="9" fill="#fff"/><path d="M5 9h7M9 5.5 12.5 9 9 12.5" stroke="#8a3fa8" stroke-width="2.2" fill="none" stroke-linecap="round" stroke-linejoin="round"/></svg>
        FREE DEMO
      </span>
      <span class="action action-login">
        <svg viewBox="0 0 18 18"><circle cx="9" cy="9" r="9" fill="#fff"/><path d="M5 9h7M9 5.5 12.5 9 9 12.5" stroke="#f7941d" stroke-width="2.2" fill="none" stroke-linecap="round" stroke-linejoin="round"/></svg>
        LOGIN
      </span>
    </div>
  </header>

  <nav class="main-nav">
    <ul>
      <li class="is-active">HOME</li>
      <li>SOFTWARE</li>
      <li>INDUSTRIES</li>
      <li>NEWS</li>
      <li>WEBINARS</li>
      <li>FREE DOWNLOADS</li>
      <li>OUR STORY</li>
      <li>OUR VALUES</li>
      <li>CONTACT US</li>
    </ul>
  </nav>

  <section class="hero" role="img" aria-label="Looking up between two glass office towers against a blue sky">
    <div class="hero-caption">Every company is a media company<br>Empower Your Now!</div>
    <div class="hero-cta">LEARN MORE</div>
  </section>

  <p class="tagline">Fast and easy way to send press releases, manage your<br>news page &amp; nurture your reputation</p>

  <section class="features">
    <article class="feature">
      <h2>Cloud-based</h2>
      <svg viewBox="0 0 80 76">
        <defs><linearGradient id="gCloud" x1="0" y1="0" x2="0" y2="1"><stop offset="0" stop-color="#2bb266"/><stop offset="1" stop-color="#1d8a4a"/></linearGradient></defs>
        <path d="M18 64a16 16 0 0 1-2-31.9A22 22 0 0 1 58 26a17 17 0 0 1 4 38z" fill="url(#gCloud)"/>
        <path d="M40 30 26 46h9v14h10V46h9z" fill="#fff"/>
      </svg>
      <p>Manage your marketing and PR campaigns with easy use tools from any device.</p>
    </article>
    <article class="feature">
      <h2>Big Database</h2>
      <svg viewBox="0 0 80 76">
        <defs><linearGradient id="gDb" x1="0" y1="0" x2="0" y2="1"><stop offset="0" stop-color="#2bb266"/><stop offset="1" stop-color="#1d8a4a"/></linearGradient></defs>
        <ellipse cx="40" cy="12" rx="32" ry="10" fill="url(#gDb)"/>
        <path d="M8 18c0 6 14 11 32 11s32-5 32-11v12c0 6-14 11-32 11S8 36 8 30z" fill="url(#gDb)"/>
        <path d="M8 36c0 6 14 11 32 11s32-5 32-11v12c0 6-14 11-32 11S8 54 8 48z" fill="url(#gDb)"/>
        <path d="M8 54c0 6 14 11 32 11s32-5 32-11v8c0 6-14 11-32 11S8 68 8 62z" fill="url(#gDb)"/>
      </svg>
      <p>Database of 20,000 journalists with the added ability to be able to add your own.</p>
    </article>
    <article class="feature">
      <h2>Secure &amp; Safe</h2>
      <svg viewBox="0 0 80 76">
        <defs><linearGradient id="gSafe" x1="0" y1="0" x2="0" y2="1"><stop offset="0" stop-color="#2bb266"/><stop offset="1" stop-color="#1d8a4a"/></linearGradient></defs>
        <path d="M4 4h28l6 7h38v61H4z" fill="url(#gSafe)"/>
        <rect x="30" y="40" width="20" height="16" rx="2" fill="#fff"/>
        <path d="M34 40v-5a6 6 0 0 1 12 0v5" stroke="#fff" stroke-width="3.5" fill="none"/>
      </svg>
      <p>Daily backups and hosting on Hostwell dedicated servers keep your data safe.</p>
    </article>
    <article class="feature">
      <h2>Save Time</h2>
      <svg viewBox="0 0 80 76">
        <defs><linearGradient id="gTime" x1="0" y1="0" x2="0" y2="1"><stop offset="0" stop-color="#2bb266"/><stop offset="1" stop-color="#1d8a4a"/></linearGradient></defs>
        <path d="M40 6a34 34 0 1 1-30 18" stroke="url(#gTime)" stroke-width="8" fill="none"/>
        <path d="M22 4 40 6 30 20z" fill="url(#gTime)"/>
        <path d="M40 20v20h-16" stroke="url(#gTime)" stroke-width="6" fill="none"/>
      </svg>
      <p>Kelmarbyte brilliantly wins media coverage and distributes your news in minutes.</p>
    </article>
  </section>
</body>
</html>
```